Need Bold and Innovative Book Cover

Hi,

I am in need of a bold and innovative book cover to catch the attention of people.

Here is what the book is about:

Title: Quiet Lantern - Taming Clutter To Build Your Finest Season Yet

Author: Lifeguard Dan Petrovski

This book is about how to eliminate overwhelm, stress, and information overload from your life. This book is a guide to teach people how I made my life better by getting rid of all kinds of stress, overwhelm, etc.

I have an information product that we created the book from. You can watch the video here to have an even better idea.

http://quietlanternbook.example/

In addition here is an instructional video about what I would like to see for the cover.

http://clipviewer.example/t/QzrTbPmoVfK

I look forward to the designs.

Thanks!

Reason: Several designers needed a bit more time.

Reason: Need more time to work on this. Dan

Target Market(s)

Busy people who want to get more done.

Industry/Entity Type

Product

Requirements
Must have
• Model the info product so it all ties in but also use your own creativity.

```html
<!DOCTYPE html>
<html lang="en">
<head>
<meta charset="utf-8">
<title>Quiet Lantern – Book Cover</title>
<link href="https://fonts.googleapis.com/css2?family=Alfa+Slab+One&family=Oswald:wght@500&family=Tinos:wght@400;700&display=swap" rel="stylesheet">
<style>
  :root {
    --backdrop: #ececec;
    --cover: #151515;
    --spine: #1d1d1d;
    --ink-white: #f4f4f4;
    --ink-grey: #d4d4d4;
    --body-grey: #c9c9c9;
    --spine-muted: #9a9a9a;
    --box: #e6e6e6;
    --box-ink: #222222;
    --art-light: #5a5a5a;
    --art-mid: #3d3d3d;
    --art-dark: #262626;
  }
  * { margin: 0; padding: 0; box-sizing: border-box; }
  html, body { width: 1200px; height: 800px; overflow: hidden; }
  body {
    position: relative;
    background: radial-gradient(ellipse at 60% 45%, #f7f7f7 0%, var(--backdrop) 70%, #dedede 100%);
    font-family: "Tinos", "Times New Roman", serif;
  }
  h1, h2 { font-weight: 400; font-size: inherit; }

  /* ---------- back cover ---------- */
  .back-cover {
    position: absolute; left: 170px; top: 82px;
    width: 340px; height: 543px;
    background: var(--cover);
    box-shadow: 0 8px 24px rgba(0,0,0,.25);
    color: var(--ink-grey);
  }
  .back-cover .author {
    position: absolute; right: 26px; top: 16px;
    font-weight: 700; font-size: 13px; color: var(--ink-grey);
  }
  .back-cover .title {
    position: absolute; left: 0; right: 0; top: 38px;
    text-align: center;
    font-family: "Alfa Slab One", "Rockwell", serif;
    font-size: 44px; line-height: 50px; letter-spacing: 1px;
    color: var(--ink-grey);
    text-transform: uppercase;
  }
  .back-cover .subtitle {
    position: absolute; left: 0; right: 0; top: 146px;
    text-align: center;
    font-family: "Oswald", "Arial Narrow", sans-serif;
    font-size: 11px; letter-spacing: .6px; color: var(--ink-grey);
    text-transform: uppercase;
  }
  .back-cover .blurb {
    position: absolute; left: 22px; right: 22px; top: 176px;
    font-size: 11.6px; line-height: 15.6px;
    text-align: justify; text-align-last: center;
    color: var(--body-grey);
  }
  .back-cover .placeholder {
    position: absolute; top: 463px;
    width: 112px; height: 50px;
    background: var(--box);
    display: flex; align-items: center; justify-content: center;
    font-weight: 700; font-size: 12px; color: var(--box-ink);
  }
  .back-cover .placeholder.logo { left: 34px; }
  .back-cover .placeholder.isbn { left: 208px; width: 116px; }

  /* ---------- spine ---------- */
  .spine {
    position: absolute; left: 605px; top: 62px;
    width: 36px; height: 638px;
    background: var(--spine);
    box-shadow: 0 8px 24px rgba(0,0,0,.25);
  }
  .spine .spine-title {
    position: absolute; left: 50%; top: 12px;
    writing-mode: vertical-rl;
    transform: translateX(-50%);
    font-family: "Alfa Slab One", "Rockwell", serif;
    font-size: 25px; letter-spacing: 1px; color: var(--ink-white);
    text-transform: uppercase; white-space: nowrap;
  }
  .spine .spine-author {
    position: absolute; left: 50%; top: 488px;
    writing-mode: vertical-rl;
    transform: translateX(-50%);
    font-size: 10px; color: var(--spine-muted); white-space: nowrap;
  }

  /* ---------- front cover ---------- */
  .front-cover {
    position: absolute; left: 641px; top: 62px;
    width: 389px; height: 638px;
    background: var(--cover);
    box-shadow: 6px 10px 26px rgba(0,0,0,.28);
    overflow: hidden;
  }
  .front-cover .author {
    position: absolute; right: 20px; top: 17px;
    font-weight: 700; font-size: 14.5px; color: var(--ink-white);
  }
  .front-cover .portrait-art {
    position: absolute; left: 0; top: 100px;
    width: 320px; height: 538px;
    background: linear-gradient(160deg, var(--art-light) 0%, var(--art-mid) 45%, var(--art-dark) 100%);
  }
  .front-cover .title-top,
  .front-cover .title-bottom {
    position: absolute;
    font-family: "Alfa Slab One", "Rockwell", serif;
    letter-spacing: 1px; line-height: 1; white-space: nowrap;
    color: var(--ink-white); text-transform: uppercase;
    text-shadow: 2px 2px 0 #000;
    transform-origin: left center;
  }
  .front-cover .title-top {
    left: 8px; top: 40px;
    font-size: 56px;
    transform: rotate(4deg);
  }
  .front-cover .title-bottom {
    left: 192px; top: 126px;
    font-size: 36px;
    transform: rotate(24deg);
  }
  .front-cover .subtitle {
    position: absolute; left: 222px; top: 270px; width: 160px;
    text-align: center;
    font-family: "Oswald", "Arial Narrow", sans-serif;
    font-size: 19px; line-height: 24px; letter-spacing: .5px;
    color: var(--ink-white); text-transform: uppercase;
  }
</style>
</head>
<body>

  <section class="back-cover" aria-label="Back cover">
    <p class="author">Lifeguard Dan Petrovski's</p>
    <h2 class="title">Quiet<br>Lantern</h2>
    <p class="subtitle">Taming clutter to build your finest season yet</p>
    <p class="blurb">Lorem ipsum dolor sit amet, consectetur adipisicing elit, sed do eiusmod tempor incididunt ut labore et dolore magna aliqua. Ut enim ad minim veniam, quis nostrud exercitation. Lorem ipsum dolor sit amet, consectetur adipisicing elit, sed do eiusmod tempor incididunt ut labore et dolore magna aliqua. Ut enim ad minim veniam, quis nostrud exercitation. Lorem ipsum dolor sit amet, consectetur adipisicing elit, sed do eiusmod tempor incididunt ut labore et dolore magna aliqua. Ut enim ad minim veniam, quis nostrud exercitation. Lorem ipsum dolor sit amet, consectetur adipisicing elit, sed do eiusmod tempor incididunt ut labore et dolore magna aliqua. Ut enim ad minim veniam, quis nostrud exercitation. Lorem ipsum dolor sit amet, consectetur adipisicing elit, sed do eiusmod tempor incididunt ut labore et dolore magna aliqua. Ut enim ad minim veniam, quis nostrud exercitation. Lorem ipsum dolor sit amet, consectetur adipisicing elit, sed do eiusmod tempor incididunt ut labore et dolore magna aliqua. Ut enim ad minim veniam, quis nostrud exercitation.</p>
    <div class="placeholder logo">LOGO</div>
    <div class="placeholder isbn">ISBN</div>
  </section>

  <aside class="spine" aria-label="Spine">
    <span class="spine-title">Quiet Lantern</span>
    <span class="spine-author">Lifeguard Dan Petrovski</span>
  </aside>

  <section class="front-cover" aria-label="Front cover">
    <p class="author">Lifeguard Dan Petrovski's</p>
    <div class="portrait-art" role="img" aria-label="Distressed white portrait of the author holding a finger to his lips, built from a repeated word pattern"></div>
    <h1>
      <span class="title-top">Quiet</span>
      <span class="title-bottom">Lantern</span>
    </h1>
    <p class="subtitle">Taming clutter<br>to build your<br>finest season yet</p>
  </section>

</body>
</html>
```